Lantern Brook Teas needs 5 Cylinder Packaging Labels

I am looking for 5 variations of cylinder label designs for my herbal tea company, to use on eco-friendly matte black cardboard cylinder packaging.
Lantern Brook Teas is launching soon and will have 3 wellness teas, as well as 2 ritual teas. All organic and eco-conscious.
Wellness: Quiet Harbor Mix (calming and soothing), Sparkrise Tea (energetic and fresh) and Petal Cycle Tea (for women's wellbeing).
Ritual Teas: 'Stillpoint' (clear and focused, to prepare for meditation and ritual work) and 'Kindle' (energising and powerful, to use during ritual and magical workings).
I am looking for an earthy, herbal, yet also an antiqued mysterious look, to compliment the brand's sparkrise. I am an sparkrise worker and charge the herbal blends with intention for customers. I would like the packaging to promote a magical and witchy feel to an organic herbal brand.
I also love the idea of watercolour being used in the design, but this isn't a dealbreaker. I am very open to the designer's interpretation of my brand!
I would like to see each tea blend have a different colour to suit the type of tea (eg: Kindle ritual tea using purples, Stillpoint ritual tea using greens, petal cycle tea using pinks, sparkrise tea using oranges, quiet harbor mix using blues).
I would love to see some rich, jewel tones incorporated in this product design!
I have added a few inspiration photos to this brief, as well as a logo mock-up which I would like used in the design. I would also like to see the brand name ‘Lantern Brook Teas’ with this logo.
Target Market(s)
My ideal customer is spiritually connected (yoga, meditation, witches, healers, etc), interested in holistic wellness and environmentally driven.
Industry/Entity Type
Tea, Holistic Wellness
Requirements
Must have
- 5 variations of a cohesive herbal tea brand label. I will need to include ingredients, brewing instructions and product weight on the label. I would also like to see indications that the packaging is eco-friendly and made in Australia.
Nice to have
- I would like to see some deep jewel tones incorporated in the label designs, with perhaps some gold for the ritual teas, to have them stand out as our luxury range.

```html
<!DOCTYPE html>
<html lang="en">
<head>
<meta charset="utf-8">
<title>Lantern Brook Teas – Cylinder Labels</title>
<link rel="stylesheet" href="https://fonts.googleapis.com/css2?family=Cormorant+Garamond:wght@400;500&family=Great+Vibes&family=Montserrat:wght@400;600&family=Playfair+Display:wght@700&display=swap">
<style>
  :root {
    --page: #ffffff;
    --ink: #f4f1ec;
    --rule: rgba(236, 232, 226, 0.7);
    --night: #07070a;
    --gold: #c99a52;
    --blue: #1aa6e0;
    --blue-deep: #0d4f86;
    --orange: #e8832c;
    --orange-deep: #8a2f14;
    --pink: #d8268a;
    --pink-deep: #6a1460;
    --green: #1e9c86;
    --green-deep: #0b4f55;
    --violet: #7b4bb7;
    --violet-deep: #2c2466;
  }
  * { box-sizing: border-box; margin: 0; padding: 0; }
  html, body { width: 1200px; height: 1200px; overflow: hidden; background: var(--page); }
  .sheet { position: relative; width: 1200px; height: 1200px; }

  .label {
    position: absolute; width: 342px; height: 524px; overflow: hidden;
    background: var(--night); color: var(--ink);
  }
  .label--harbor  { left: 36px;  top: 38px;  --tone: var(--blue);   --tone-deep: var(--blue-deep); }
  .label--spark   { left: 427px; top: 38px;  --tone: var(--orange); --tone-deep: var(--orange-deep); }
  .label--petal   { left: 818px; top: 38px;  --tone: var(--pink);   --tone-deep: var(--pink-deep); }
  .label--still   { left: 236px; top: 639px; --tone: var(--green);  --tone-deep: var(--green-deep); }
  .label--kindle  { left: 636px; top: 639px; --tone: var(--violet); --tone-deep: var(--violet-deep); }

  .label__wash {
    position: absolute; inset: 0;
    background:
      radial-gradient(ellipse 60% 30% at 20% 8%, var(--tone-deep), transparent 70%),
      radial-gradient(ellipse 45% 40% at 90% 25%, var(--tone), transparent 70%),
      radial-gradient(ellipse 55% 35% at 10% 78%, var(--tone), transparent 70%),
      radial-gradient(ellipse 50% 40% at 85% 70%, var(--tone-deep), transparent 72%),
      radial-gradient(ellipse 40% 25% at 55% 45%, var(--tone-deep), transparent 75%),
      var(--night);
  }
  .label__frame { position: absolute; inset: 0; }

  .label__range {
    position: absolute; top: 60px; left: 0; right: 0; text-align: center;
    font-family: "Great Vibes", cursive; font-size: 30px; line-height: 1;
  }
  .label__mark {
    position: absolute; top: 128px; left: 50%; width: 22px; height: 22px;
    margin-left: -11px; border: 1.5px solid var(--ink); border-radius: 50%;
  }
  .label__brand {
    position: absolute; top: 164px; left: 0; right: 0; text-align: center;
    font-family: "Cormorant Garamond", serif; font-weight: 500;
    font-size: 34px; line-height: 1.05; color: var(--ink);
  }

  .label__product {
    position: absolute; top: 312px; left: 58px; width: 137px; text-align: center;
    font-family: "Playfair Display", serif; font-weight: 700;
    font-size: 16px; letter-spacing: 0.06em; line-height: 30px; white-space: nowrap;
  }
  .label__benefit {
    position: absolute; top: 317px; left: 204px; width: 95px;
    font-family: "Montserrat", sans-serif; font-size: 8.5px; letter-spacing: 0.12em;
    line-height: 1.2; text-transform: uppercase;
  }
  .label__origin {
    position: absolute; top: 350px; left: 58px; width: 137px; text-align: center;
    font-family: "Montserrat", sans-serif; font-size: 6.5px; letter-spacing: 0.1em;
    line-height: 22px; text-transform: uppercase;
  }
  .label__weight {
    position: absolute; top: 350px; left: 195px; width: 97px; text-align: center;
    font-family: "Cormorant Garamond", serif; font-weight: 500; font-size: 16px; line-height: 22px;
  }
  .label__brewing {
    position: absolute; top: 378px; left: 52px; width: 238px; text-align: center;
    font-family: "Montserrat", sans-serif; font-size: 6.6px; letter-spacing: 0.06em;
    line-height: 1.7; text-transform: uppercase;
  }
  .label__brewing strong { font-weight: 600; }

  .label__eco {
    position: absolute; top: 452px; left: 144px; width: 52px; height: 52px; border-radius: 50%;
    background: radial-gradient(circle at 40% 35%, var(--tone), var(--tone-deep) 75%);
    border: 2px solid #1b1b1f;
  }
</style>
</head>
<body>
<main class="sheet">

  <article class="label label--harbor">
    <div class="label__wash" role="img" aria-label="Blue watercolour wash with gold splashes on black"></div>
    <svg class="label__frame" viewBox="0 0 342 524" aria-hidden="true">
      <g stroke="var(--rule)" stroke-width="0.8" fill="none">
        <line x1="42" y1="31" x2="298" y2="31"/><line x1="40" y1="60" x2="40" y2="456"/>
        <line x1="302" y1="60" x2="302" y2="456"/><line x1="42" y1="492" x2="298" y2="492"/>
        <line x1="58" y1="306" x2="292" y2="306"/><line x1="58" y1="348" x2="292" y2="348"/>
        <line x1="58" y1="373" x2="292" y2="373"/><line x1="195" y1="306" x2="195" y2="373"/>
      </g>
    </svg>
    <p class="label__range">wellness</p>
    <span class="label__mark"></span>
    <h2 class="label__brand">Lantern Brook<br>Teas</h2>
    <h3 class="label__product">quiet harbor</h3>
    <p class="label__benefit">Calming &amp; soothing</p>
    <p class="label__origin">Made in Australia</p>
    <p class="label__weight">2.oz</p>
    <p class="label__brewing"><strong>Brewing instructions:</strong> Lorem ipsum dolor sit amet, consectetuer adipiscing elit, sed diam. Lorem ipsum dolor sit amet, consectetuer adipiscing elit, sed diam.</p>
    <span class="label__eco" role="img" aria-label="Eco-friendly seal"></span>
  </article>

  <article class="label label--spark">
    <div class="label__wash" role="img" aria-label="Orange watercolour wash with gold splashes on black"></div>
    <svg class="label__frame" viewBox="0 0 342 524" aria-hidden="true">
      <g stroke="var(--rule)" stroke-width="0.8" fill="none">
        <line x1="42" y1="31" x2="298" y2="31"/><line x1="40" y1="60" x2="40" y2="456"/>
        <line x1="302" y1="60" x2="302" y2="456"/><line x1="42" y1="492" x2="298" y2="492"/>
        <line x1="58" y1="306" x2="292" y2="306"/><line x1="58" y1="348" x2="292" y2="348"/>
        <line x1="58" y1="373" x2="292" y2="373"/><line x1="195" y1="306" x2="195" y2="373"/>
      </g>
    </svg>
    <p class="label__range">wellness</p>
    <span class="label__mark"></span>
    <h2 class="label__brand">Lantern Brook<br>Teas</h2>
    <h3 class="label__product">sparkrise</h3>
    <p class="label__benefit">Energetic &amp; fresh</p>
    <p class="label__origin">Made in Australia</p>
    <p class="label__weight">2.oz</p>
    <p class="label__brewing"><strong>Brewing instructions:</strong> Lorem ipsum dolor sit amet, consectetuer adipiscing elit, sed diam. Lorem ipsum dolor sit amet, consectetuer adipiscing elit, sed diam.</p>
    <span class="label__eco" role="img" aria-label="Eco-friendly seal"></span>
  </article>

  <article class="label label--petal">
    <div class="label__wash" role="img" aria-label="Magenta watercolour wash with gold splashes on black"></div>
    <svg class="label__frame" viewBox="0 0 342 524" aria-hidden="true">
      <g stroke="var(--rule)" stroke-width="0.8" fill="none">
        <line x1="42" y1="31" x2="298" y2="31"/><line x1="40" y1="60" x2="40" y2="456"/>
        <line x1="302" y1="60" x2="302" y2="456"/><line x1="42" y1="492" x2="298" y2="492"/>
        <line x1="58" y1="306" x2="292" y2="306"/><line x1="58" y1="348" x2="292" y2="348"/>
        <line x1="58" y1="373" x2="292" y2="373"/><line x1="195" y1="306" x2="195" y2="373"/>
      </g>
    </svg>
    <p class="label__range">wellness</p>
    <span class="label__mark"></span>
    <h2 class="label__brand">Lantern Brook<br>Teas</h2>
    <h3 class="label__product">petal cycle</h3>
    <p class="label__benefit">Feminine wellbeing</p>
    <p class="label__origin">Made in Australia</p>
    <p class="label__weight">2.oz</p>
    <p class="label__brewing"><strong>Brewing instructions:</strong> Lorem ipsum dolor sit amet, consectetuer adipiscing elit, sed diam. Lorem ipsum dolor sit amet, consectetuer adipiscing elit, sed diam.</p>
    <span class="label__eco" role="img" aria-label="Eco-friendly seal"></span>
  </article>

  <article class="label label--still">
    <div class="label__wash" role="img" aria-label="Emerald watercolour wash with gold splashes on black"></div>
    <svg class="label__frame" viewBox="0 0 342 524" aria-hidden="true">
      <g stroke="var(--rule)" stroke-width="0.8" fill="none">
        <line x1="42" y1="31" x2="298" y2="31"/><line x1="40" y1="60" x2="40" y2="456"/>
        <line x1="302" y1="60" x2="302" y2="456"/><line x1="42" y1="492" x2="298" y2="492"/>
        <line x1="58" y1="306" x2="292" y2="306"/><line x1="58" y1="348" x2="292" y2="348"/>
        <line x1="58" y1="373" x2="292" y2="373"/><line x1="195" y1="306" x2="195" y2="373"/>
      </g>
    </svg>
    <p class="label__range">ritual</p>
    <span class="label__mark"></span>
    <h2 class="label__brand">Lantern Brook<br>Teas</h2>
    <h3 class="label__product">stillpoint</h3>
    <p class="label__benefit">Fresh &amp; focused</p>
    <p class="label__origin">Made in Australia</p>
    <p class="label__weight">2.oz</p>
    <p class="label__brewing"><strong>Brewing instructions:</strong> Lorem ipsum dolor sit amet, consectetuer adipiscing elit, sed diam. Lorem ipsum dolor sit amet, consectetuer adipiscing elit, sed diam.</p>
    <span class="label__eco" role="img" aria-label="Eco-friendly seal"></span>
  </article>

  <article class="label label--kindle">
    <div class="label__wash" role="img" aria-label="Violet watercolour wash with gold splashes on black"></div>
    <svg class="label__frame" viewBox="0 0 342 524" aria-hidden="true">
      <g stroke="var(--rule)" stroke-width="0.8" fill="none">
        <line x1="42" y1="31" x2="298" y2="31"/><line x1="40" y1="60" x2="40" y2="456"/>
        <line x1="302" y1="60" x2="302" y2="456"/><line x1="42" y1="492" x2="298" y2="492"/>
        <line x1="58" y1="306" x2="292" y2="306"/><line x1="58" y1="348" x2="292" y2="348"/>
        <line x1="58" y1="373" x2="292" y2="373"/><line x1="195" y1="306" x2="195" y2="373"/>
      </g>
    </svg>
    <p class="label__range">ritual</p>
    <span class="label__mark"></span>
    <h2 class="label__brand">Lantern Brook<br>Teas</h2>
    <h3 class="label__product">kindle</h3>
    <p class="label__benefit">Energising &amp; powerful</p>
    <p class="label__origin">Made in Australia</p>
    <p class="label__weight">2.oz</p>
    <p class="label__brewing"><strong>Brewing instructions:</strong> Lorem ipsum dolor sit amet, consectetuer adipiscing elit, sed diam. Lorem ipsum dolor sit amet, consectetuer adipiscing elit, sed diam.</p>
    <span class="label__eco" role="img" aria-label="Eco-friendly seal"></span>
  </article>

</main>
</body>
</html>
```